Corporate Design für Apotheke
Zielgruppe
Gesundheitswesen, Apotheke Zielgruppe kranke Menschen aber auch 'shopper'.
Aufgabenstellung
Das alte Logo ist leider viel zu filigran. Bei verschiedenen Druck kommt es oft nicht raus. Früher war das Logo eckig, es wurde vor Jahren mal als rund modernisiert.
Bin aber offen für alles.
Apotheke sollte grundsätzlich mit den Werten Seriosität, Vertrauen , und in unserem Fall auch Exklusivität, Premium- Segment verbunden werden. Im Anhang unser altes Logo. Ich bin zum ersten mal hier und freue mich auf kreative Vorschläge

```html
<!DOCTYPE html>
<html lang="de">
<head>
<meta charset="utf-8">
<title>Talblick Apotheke – Briefbogen</title>
<link rel="stylesheet" href="https://fonts.googleapis.com/css2?family=Jost:wght@400;500;600;700&family=Caveat:wght@500&display=swap">
<style>
  :root {
    --paper: #fafafa;
    --green-dark: #2f7f50;
    --green-bright: #4cb447;
    --green-deep: #3d9e3f;
    --text: #4d4d4d;
    --deco-light: #e2efe3;
    --deco-mid: #d5e6da;
    --white: #ffffff;
  }
  * { margin: 0; padding: 0; box-sizing: border-box; }
  html, body { width: 853px; height: 1200px; overflow: hidden; background: var(--paper); }
  body { font-family: "Jost", sans-serif; color: var(--text); }
  .letterhead { position: relative; width: 853px; height: 1200px; background: var(--paper); }
  .abs { position: absolute; }

  .fold-tick { left: 600px; top: 8px; width: 1.5px; height: 11px; background: var(--green-bright); }
  .margin-mark { left: 7px; height: 1.5px; width: 12px; background: var(--green-bright); }
  .margin-mark.hole { width: 21px; }
  .window-dot { width: 2px; height: 2px; border-radius: 50%; background: var(--green-bright); }

  .claim { left: 79px; top: 110px; font-family: "Caveat", cursive; font-weight: 500; font-size: 28px; color: var(--green-bright); }

  .brand { left: 520px; top: 86px; width: 284px; text-align: center; }
  .brand-dot { display: block; margin: 0 auto 10px; width: 50px; height: 50px; border-radius: 50%; border: 3px solid var(--green-dark); }
  .brand-name { font-weight: 700; font-size: 19px; letter-spacing: 2.2px; color: var(--green-dark); line-height: 1; }
  .brand-tagline { margin-top: 7px; font-size: 13px; color: var(--green-bright); }

  .sender-line { left: 88px; top: 183px; font-size: 12.3px; color: var(--green-dark); }

  .recipient { left: 100px; top: 220px; font-size: 12.4px; line-height: 17.2px; letter-spacing: 0.1px; }

  .contact { left: 546px; top: 236px; font-size: 12.3px; line-height: 17.2px; color: var(--green-dark); }
  .contact dl { margin-top: 12px; display: grid; grid-template-columns: 36px auto; }
  .contact dt { font-weight: 600; }

  .letter-body { left: 100px; top: 423px; width: 673px; font-size: 12.4px; line-height: 17.2px; letter-spacing: 0.1px; }
  .subject { font-weight: 600; font-size: 12.6px; margin-bottom: 35px; }
  .letter-body p { margin-bottom: 17.2px; }
  .letter-body .closing { margin-top: 34px; margin-bottom: 17.2px; }

  .watermark { left: 596px; top: 916px; width: 213px; height: 216px; }

  .footer { left: 0; top: 1132px; width: 853px; height: 68px; background: linear-gradient(90deg, var(--green-bright), var(--green-deep)); color: var(--white); font-size: 12.4px; line-height: 17.5px; padding: 15px 0 0 81px; white-space: nowrap; }
</style>
</head>
<body>
<div class="letterhead">
  <span class="abs fold-tick"></span>
  <span class="abs margin-mark" style="top:426px"></span>
  <span class="abs margin-mark hole" style="top:604px"></span>
  <span class="abs margin-mark" style="top:853px"></span>

  <p class="abs claim">… Wir sind für Sie da!</p>

  <div class="abs brand">
    <span class="brand-dot"></span>
    <p class="brand-name">TALBLICK APOTHEKE</p>
    <p class="brand-tagline">Gesundheit mitten in Lindenhausen</p>
  </div>

  <p class="abs sender-line">Talblick Apotheke | Musterstraße 1 | 79249 Lindenhausen</p>
  <span class="abs window-dot" style="left:81px;top:203px"></span>
  <span class="abs window-dot" style="left:424px;top:203px"></span>
  <span class="abs window-dot" style="left:81px;top:365px"></span>
  <span class="abs window-dot" style="left:424px;top:365px"></span>

  <address class="abs recipient" style="font-style:normal">
    Beate Müller<br>Musterstraße 1<br>01234 Musterstadt
  </address>

  <div class="abs contact">
    <p>Musterstraße 1 | 79249 Lindenhausen</p>
    <dl>
      <dt>Fon:</dt><dd>012 987 41 30</dd>
      <dt>Web:</dt><dd>talblick-apotheke.de</dd>
      <dt>Mail:</dt><dd>info@talblick-apotheke.de</dd>
    </dl>
  </div>

  <main class="abs letter-body">
    <h1 class="subject">Rechnungslegung November 2019</h1>
    <p>Sehr geehrte Frau Müller,</p>
    <p>Is evelibusant adist, simpori tatias volorem reicabore, omnitas explaut erum re officipsam aut acipic te volut fugit, apid minum fugiandant verum vellaut quibusapelit omnistrumet alitat dolecea verfere mporem restio. At facietus, con nos invel et ant, conesto de imolum, te int.</p>
    <p>Ibuscita soluptius quid quo to qui ullaut desti cumet laut et adit esequis cipit, odis vitia ditias ariorpo rionsedi dolori voluptatus nectiis dolupta speles quatemolupta vent illabor ibusdan ditaepe rissum essum rest que duciduntures est rae vendi rem que nulles int quatquodis et modignis dolorem volori ullut et ad est rem quisincid quatatur restemolupta sum labo. Ipsunt ut quiae et quiderupta sit ius.</p>
    <p>Tust et voloris non pro occus, sequiditio eum cullaci dolut restrum apelit, nonsecabo. Neque restrum hil eum ipiet debis doluptur remquam que si bero ipsunt, conectur sapit quibus sit qui ut volo beat.</p>
    <p>Cerum earcidem facepero vit, tem ent voloruntem es magnimillaut mi, to eatiunt emoloratium ut eaquis quodi am quuntibuscit minissi dolupta doloreh enietur aut quam nulliquibus explitiorem re prenda placcae essequam hilique cum etur as ut earum rerio. Ur sum ne volor autemque volori doloratus.</p>
    <p class="closing">Mit freundlichen Grüßen</p>
    <p>Ihr Team der Talblick Apotheke</p>
  </main>

  <svg class="abs watermark" viewBox="0 0 213 216" role="img" aria-label="Große, blasse Bildmarke der Apotheke als Hintergrunddekoration">
    <defs>
      <linearGradient id="decoFade" x1="0" y1="0" x2="0" y2="1">
        <stop offset="0" stop-color="#e2efe3"/>
        <stop offset="1" stop-color="#d5e6da"/>
      </linearGradient>
    </defs>
    <rect x="0" y="0" width="213" height="216" rx="6" fill="url(#decoFade)" opacity="0.7"/>
  </svg>

  <footer class="abs footer">
    Talblick Apotheke | Inhaber Apotheker Max Mustermann | USt-IdNr. DE 141 491 208 | Handelsregisternr. 12345648910<br>
    Mo – Fr 8.00 – 19.00 Uhr, Sa 10.00 – 14.00 Uhr | Bank XXXXXX | BIC XXXXXXXXXXX | IBAN DE53 2222 3333 4444 5555 66
  </footer>
</div>
</body>
</html>
```